Agriculture farming Hemp and CBD

The logo is in works with your company now, should be ready in a few days. We have our Domain (brightmeadowco.com) We would like to see incorporated seed to growth, but not necessary. we would like to nature colors and some black and green. we have our farm and will be growing and selling HEMP and CBD we are based in the state of Virginia. Would like to incorporate the words pause, play, rewind if possible but not necessary.

Target Market(s)

20 years old to elderly

Coding

Coded - Design and coding required

Number of Pages Required

3 page

Font styles to use
Serif

Requirements
Must have
• I'm not sure on the must haves, we are open to any ideas, we would definitely like to see Hemp and CBD included, may the life cycle of seed to plant. We must have a pop up asking if you are 20 years old before they can enter our site and to view or purchase our product. I want the design to be totally different than what i uploaded.
Nice to have
• Would like to see natural colors as well as black and green
Should not have
• I want

```html
<!DOCTYPE html>
<html lang="en">
<head>
<meta charset="utf-8">
<title>Bright Meadow Co – Home</title>
<link href="https://fonts.googleapis.com/css2?family=Roboto+Slab:wght@500;600;700&family=Source+Serif+4:wght@400;500;600&display=swap" rel="stylesheet">
<style>
:root{
  --green:#0bb53a;
  --green-bright:#1fd14a;
  --black:#000;
  --ink:#111;
  --grey-dark:#1d1d1d;
  --grey-foot:#2a2a2a;
  --white:#fff;
  --price:#e0252b;
  --star:#f2a516;
  --modal:#5e5e5e;
  --head:"Roboto Slab",serif;
  --body:"Source Serif 4",serif;
}
*{box-sizing:border-box;margin:0;padding:0}
html,body{width:802px;height:1200px;overflow:hidden;background:var(--white)}
.board{position:relative;width:802px;height:1200px;overflow:hidden;background:var(--white);font-family:var(--body)}
.page{position:absolute;top:54px;width:597px;height:2132px;transform-origin:0 0;transform:scale(.5115);background:var(--black);overflow:hidden;box-shadow:0 0 60px rgba(0,0,0,.18)}
.page--home{left:65.5px}
.page--gate{left:431px}
.page__content{position:absolute;inset:0}
.page--gate .page__content{filter:blur(1.6px) brightness(.32)}
.abs{position:absolute}
.h{font-family:var(--head);font-weight:600;letter-spacing:.5px;color:var(--white)}

/* nav */
.nav{left:0;top:0;width:597px;height:52px;background:rgba(255,255,255,.92)}
.brand{left:33px;top:14px;font-family:var(--head);font-weight:600;font-size:13px;color:var(--ink)}
.brand::before{content:"";display:inline-block;width:7px;height:7px;border-radius:50%;background:var(--green);margin-right:4px;vertical-align:1px}
.nav__links{left:213px;top:22px;display:flex;gap:18px;font-size:6px;color:#666;letter-spacing:.3px}
.nav__links .active{color:var(--ink);border-bottom:1.5px solid var(--green);padding-bottom:7px}
.nav__search{left:533px;top:20px;width:7px;height:7px;border:1.2px solid #555;border-radius:50%}

/* hero */
.hero{left:0;top:0;width:597px;height:345px;background:linear-gradient(180deg,#c9d69a 0%,#8aa24a 30%,#5f7f2b 60%,#3b5a1a 100%)}
.hero__cut{left:0;top:0}
.hero__title{left:0;top:115px;width:597px;text-align:center;font-size:24px;text-shadow:0 1px 4px rgba(0,0,0,.45)}
.hero__sub{left:0;top:150px;width:597px;text-align:center;font-size:8.5px;line-height:12px;color:var(--white)}

/* about */
.about__img{left:298px;top:345px;width:299px;height:350px;background:linear-gradient(160deg,#cfc9bd 0%,#e0b978 35%,#7d8a42 65%,#3f5520 100%)}
.about__title{left:55px;top:404px;font-size:18px}
.about__lead{left:55px;top:433px;width:215px;font-size:10px;line-height:15px;color:var(--white)}
.about__body{left:55px;top:475px;width:215px;font-size:7px;line-height:13.5px;color:#e5e5e5}
.about__body p+p{margin-top:8px}
.btn{background:var(--green);color:var(--white);font-size:6.5px;font-weight:500;text-align:center;letter-spacing:.3px}
.about__btn{left:55px;top:612px;width:94px;height:20px;border-radius:10px;line-height:20px}

/* why */
.why{left:0;top:695px;width:597px;height:305px;background:linear-gradient(100deg,#2f5a16 0%,#7fab2b 25%,#c8df9a 48%,#e9efc6 70%,#e6e3a2 100%)}
.why__title{left:325px;top:744px;font-size:18px;color:var(--ink)}
.why__body{left:325px;top:775px;width:215px;font-size:7px;line-height:13.5px;color:#333}
.why__icons{left:318px;top:900px;display:flex;gap:30px}
.why__item{width:58px;text-align:center;font-size:6.2px;color:#444}
.why__item svg{display:block;margin:0 auto 8px}

/* products */
.products__title{left:0;top:1046px;width:597px;text-align:center;font-size:18px}
.card{top:1094px;width:162px;height:272px;text-align:center}
.card--active{background:var(--white);border-radius:3px}
.card__img{position:absolute;left:28px;top:12px;width:106px;height:93px}
.card__name{position:absolute;left:0;top:120px;width:162px;font-size:8px;color:#666}
.card:not(.card--active) .card__name{color:#333}
.card__price{position:absolute;left:0;top:134px;width:162px;font-size:11px;color:var(--price)}
.card__rating{position:absolute;left:0;top:153px;width:162px;font-size:7px;color:#555}
.card:not(.card--active) .card__rating{color:var(--white)}
.card__rating b{color:var(--star);letter-spacing:-.5px;margin-right:4px;font-weight:400}
.opt{position:absolute;left:15px;width:140px;text-align:left;font-size:5.6px;color:#444;display:flex;align-items:center;gap:6px;white-space:nowrap}
.card:not(.card--active) .opt{color:var(--white)}
.box{width:6px;height:6px;border:1px solid #666;display:inline-block;flex:none;position:relative;background:var(--white)}
.box--on::after{content:"";position:absolute;inset:1px;background:#111}
.card__details{position:absolute;left:0;top:207px;width:162px;font-size:5.6px;color:#444;display:flex;justify-content:center;align-items:center;gap:3px}
.card:not(.card--active) .card__details{color:var(--white)}
.card__btn{position:absolute;left:42px;top:227px;width:78px;height:23px;line-height:23px}
.dots{display:flex;gap:8px}
.dot{width:6px;height:6px;border-radius:50%;border:1px solid #bbb}
.dot--on{background:var(--green);border-color:var(--green)}

/* testimonials */
.testi{left:0;top:1443px;width:597px;height:357px;background:var(--grey-dark)}
.testi__title{left:0;top:1491px;width:597px;text-align:center;font-size:18px}
.quote{top:1546px;height:170px;background:var(--black);text-align:center}
.quote__avatar{position:absolute;top:15px;width:48px;height:48px;border-radius:50%;border:2px solid var(--white);background:linear-gradient(#9fb7c7,#5f7890)}
.quote__mark{position:absolute;top:38px;font-family:var(--head);font-size:30px;color:#1d5c2b;font-weight:700;line-height:1}
.quote__name{position:absolute;top:73px;width:100%;font-size:7.5px;color:var(--white)}
.quote__role{position:absolute;top:88px;width:100%;font-size:5.6px;color:#888;font-style:italic}
.quote__text{position:absolute;top:110px;font-size:6.4px;line-height:11.5px;color:#cfcfcf;white-space:nowrap}

/* partners */
.partners__title{left:0;top:1849px;width:597px;text-align:center;font-size:18px}
.partner{top:1896px;height:38px;display:flex;align-items:center;gap:5px;font-family:var(--head);font-weight:500;font-size:18px;color:#9a9a9a}
.partner i{width:12px;height:12px;border-radius:50%;background:#9a9a9a;display:inline-block}
.partner--on{background:var(--white);border-radius:3px;color:var(--ink);padding:0 12px}
.partner--on i{background:#e64a7a}

/* footer */
.foot{left:0;top:1980px;width:597px;height:152px}
.foot__links{left:0;top:2053px;width:597px;display:flex;justify-content:center;gap:17px;font-size:6px;color:var(--white)}
.foot__social{left:0;top:2077px;width:597px;display:flex;justify-content:center;gap:10px}
.foot__social span{width:7px;height:7px;border-radius:50%;background:var(--white)}
.foot__copy{left:0;top:2113px;width:597px;text-align:center;font-size:5.5px;color:var(--white)}

/* age gate */
.gate{left:149px;top:373px;width:300px;height:229px;background:var(--modal);text-align:center}
.gate__close{position:absolute;right:10px;top:8px;font-size:8px;color:var(--white)}
.gate__brand{position:absolute;left:0;top:30px;width:300px;font-family:var(--head);font-weight:600;font-size:13px;color:var(--white)}
.gate__brand::before{content:"";display:inline-block;width:7px;height:7px;border-radius:50%;background:var(--green-bright);margin-right:4px;vertical-align:1px}
.gate__q{position:absolute;left:0;top:80px;width:300px;font-family:var(--head);font-weight:500;font-size:14px;color:var(--white)}
.gate__btn{position:absolute;top:120px;width:74px;height:25px;line-height:25px;text-align:left;padding-left:11px;font-size:6.5px}
.gate__btn::after{content:"";position:absolute;right:15px;top:12px;width:8px;height:1px;background:var(--white)}
.gate__note{position:absolute;left:0;top:177px;width:300px;font-size:6.3px;color:var(--white)}
</style>
</head>
<body>
<div class="board">

  <!-- Home page -->
  <div class="page page--home">
    <div class="page__content">
      <div class="abs hero" role="img" aria-label="Photo of a hemp field at sunset"></div>
      <svg class="abs hero__cut" width="597" height="460" viewBox="0 0 597 460"><polygon points="0,320 597,270 597,345 0,345" fill="#000"/></svg>
      <div class="abs nav"></div>
      <div class="abs brand">brightmeadowco.com</div>
      <nav class="abs nav__links"><span class="active">HOME</span><span>ABOUT</span><span>OUR PRODUCTS</span><span>BLOG</span><span>TESTIMONIALS</span><span>CONTACT US &nbsp;|</span></nav>
      <div class="abs nav__search"></div>
      <h1 class="abs h hero__title">BRIGHT MEADOW CO</h1>
      <p class="abs hero__sub">Consectetur adipiscing elit, sed do eiusmod<br>tempor incididunt ut labore</p>

      <div class="abs about__img" role="img" aria-label="Photo of a researcher with a clipboard in a hemp field"></div>
      <h2 class="abs h about__title">ABOUT US</h2>
      <p class="abs about__lead">Beatae vitae dicta sunt explicaboemo enim ipsam voluptatem quia</p>
      <div class="abs about__body">
        <p>Sed ut perspiciatis unde omnis iste natus error sit voluptatem accusantium doloremque laudantium, totam rem aperiam, eaque ipsa quae ab illo inventore veritatis et quasi architecto beatae vitae dicta sunt explicabo. Nemo enim ipsam voluptatem quia.</p>
        <p>Dadipisci velit, sed quia non numquam eius modi tempora incidunt ut labore et dolore magnam aliquam quaerat voluptatem. Ut enim ad minima</p>
      </div>
      <div class="abs btn about__btn">READ MORE</div>

      <div class="abs why" role="img" aria-label="Photo of hemp leaves in soft sunlight"></div>
      <h2 class="abs h why__title">WHY CHOOSE US</h2>
      <p class="abs why__body">Eanis iste natus error sit voluptatem accusantium doloremque laudantium, totam rem aperiam, eaque ipsa quae ab illo inventore veritatis et quasi architecto beatae vitae dicta sunt explicabo. Nemo enim ipsam voluptatem quia voluptas sit aspernatur aut odit aut fugit, sed quia consequuntur magni dolores eos qui ratione voluptatem sequi nesciunt. Neque porro quisquam.</p>
      <div class="abs why__icons">
        <div class="why__item"><svg width="38" height="24" viewBox="0 0 38 24" fill="none" stroke="#0bb53a" stroke-width="1.3"><polygon points="8,6 14,9 14,16 8,19 2,16 2,9"/><polygon points="18,12 24,15 24,22 18,24 12,22 12,15"/><text x="24" y="8" font-size="7" fill="#0bb53a" stroke="none" font-family="Roboto Slab, serif">CBD</text><path d="M24 18 h12"/></svg>Episcing Ullit</div>
        <div class="why__item"><svg width="26" height="26" viewBox="0 0 26 26" fill="none" stroke="#0bb53a" stroke-width="1.3"><path d="M11 2h6M12 2v8L5 23h16L14 10V2"/><circle cx="10" cy="18" r="3"/></svg>Auntur magni</div>
        <div class="why__item"><svg width="20" height="28" viewBox="0 0 20 28" fill="none" stroke="#0bb53a" stroke-width="1.3"><rect x="7" y="1" width="6" height="5"/><rect x="4" y="6" width="12" height="21" rx="2"/><path d="M10 12v10M7 16c2 0 3 2 3 4M13 16c-2 0-3 2-3 4"/></svg>Numquam eius</div>
      </div>

      <h2 class="abs h products__title">OUR PRODUCTS</h2>
      <div class="abs card card--active" style="left:45px">
        <div class="card__img" role="img" aria-label="Photo of CBD dropper bottles" style="background:linear-gradient(135deg,#f6e2e4,#e9cfd2 60%,#3a3a3a)"></div>
        <div class="card__name">FLOWERS</div><div class="card__price">$7.25 USD</div>
        <div class="card__rating"><b>★★★★★</b>12 Reviews</div>
        <div class="opt" style="top:175px"><span class="box box--on"></span>One - time purchase: $7.25USD</div>
        <div class="opt" style="top:191px"><span class="box"></span>Subscribe &amp; save (10%): $6.55USD</div>
        <div class="card__details"><svg width="5" height="5" viewBox="0 0 5 5"><circle cx="1" cy="4" r="1" fill="currentColor"/><path d="M0 2a3 3 0 0 1 3 3M0 0a5 5 0 0 1 5 5" stroke="currentColor" stroke-width=".7" fill="none"/></svg>Subscription Details</div>
        <div class="btn card__btn">ADD TO CART</div>
      </div>
      <div class="abs card" style="left:218px">
        <div class="card__img" role="img" aria-label="Photo of a CBD bottle with hemp leaves" style="background:linear-gradient(135deg,#bfe6cf,#8fd2a8 50%,#b0552a 80%)"></div>
        <div class="card__name">FLOWERS</div><div class="card__price">$7.25 USD</div>
        <div class="card__rating"><b>★★★★★</b>12 Reviews</div>
        <div class="opt" style="top:175px"><span class="box box--on"></span>One - time purchase: $7.25USD</div>
        <div class="opt" style="top:191px"><span class="box"></span>Subscribe &amp; save (10%): $6.55USD</div>
        <div class="card__details"><svg width="5" height="5" viewBox="0 0 5 5"><circle cx="1" cy="4" r="1" fill="currentColor"/><path d="M0 2a3 3 0 0 1 3 3M0 0a5 5 0 0 1 5 5" stroke="currentColor" stroke-width=".7" fill="none"/></svg>Subscription Details</div>
        <div class="btn card__btn">ADD TO CART</div>
      </div>
      <div class="abs card" style="left:391px">
        <div class="card__img" role="img" aria-label="Photo of a jar of hemp oil and leaves" style="background:linear-gradient(180deg,#c9a977,#b08b5a 55%,#6f7a3a 80%,#d9c06a)"></div>
        <div class="card__name">FLOWERS</div><div class="card__price">$7.25 USD</div>
        <div class="card__rating"><b>★★★★★</b>12 Reviews</div>
        <div class="opt" style="top:175px"><span class="box box--on"></span>One - time purchase: $7.25USD</div>
        <div class="opt" style="top:191px"><span class="box"></span>Subscribe &amp; save (10%): $6.55USD</div>
        <div class="card__details"><svg width="5" height="5" viewBox="0 0 5 5"><circle cx="1" cy="4" r="1" fill="currentColor"/><path d="M0 2a3 3 0 0 1 3 3M0 0a5 5 0 0 1 5 5" stroke="currentColor" stroke-width=".7" fill="none"/></svg>Subscription Details</div>
        <div class="btn card__btn">ADD TO CART</div>
      </div>
      <div class="abs dots" style="left:281px;top:1386px"><span class="dot dot--on"></span><span class="dot"></span><span class="dot"></span></div>

      <div class="abs testi"></div>
      <h2 class="abs h testi__title">TESTIMONIALS</h2>
      <div class="abs quote" style="left:0;width:161px">
        <div class="quote__avatar" style="left:24px" role="img" aria-label="Customer portrait"></div>
        <div class="quote__name">Daniel R Whitfield</div><div class="quote__role">Dosng, CEO</div>
        <div class="quote__text" style="right:10px;text-align:right">unde omnis iste natus error sit voluptatem<br>oloremque laudantium, totam rem aperiam,<br>ue ipsa quae ab illo inventoreta"</div>
      </div>
      <div class="abs quote" style="left:187px;width:224px">
        <div class="quote__mark" style="left:28px">“</div>
        <div class="quote__avatar" style="left:88px" role="img" aria-label="Customer portrait"></div>
        <div class="quote__name">Marcus T Ellery</div><div class="quote__role">Dosng, CEO</div>
        <div class="quote__text" style="left:0;width:224px">"Perspiciatis unde omnis iste natus error sit voluptatem<br>accusantium doloremque laudantium, totam rem aperiam,<br>eaque ipsa quae ab illo inventore veritatis et quasi<br>architecto beatae vitae dicta"</div>
      </div>
      <div class="abs quote" style="left:437px;width:224px">
        <div class="quote__mark" style="left:28px">“</div>
        <div class="quote__avatar" style="left:88px" role="img" aria-label="Customer portrait"></div>
        <div class="quote__name">Nina J Okafor</div><div class="quote__role">Dosng, CEO</div>
        <div class="quote__text" style="left:0;width:224px">"Roe omnis iste natseklus error sit vo<br>accusantium doloremque laudantium, tota<br>eaque ipsa quae ab illo inventore verit<br>architecto dicta"</div>
      </div>
      <div class="abs dots" style="left:273px;top:1743px"><span class="dot"></span><span class="dot dot--on"></span><span class="dot"></span><span class="dot"></span></div>

      <h2 class="abs h partners__title">OUR PARTNERS</h2>
      <div class="abs partner" style="left:18px"><i></i>Orbis</div>
      <div class="abs partner partner--on" style="left:122px;width:108px"><i></i>Velda</div>
      <div class="abs partner" style="left:260px"><i></i>Korra</div>
      <div class="abs partner" style="left:378px"><i></i>Lunet</div>
      <div class="abs partner" style="left:498px;font-size:13px;letter-spacing:1.5px"><i></i>TALLOW</div>
      <div class="abs dots" style="left:281px;top:1947px"><span class="dot dot--on"></span><span class="dot"></span><span class="dot"></span></div>

      <svg class="abs foot" width="597" height="152" viewBox="0 0 597 152"><polygon points="0,5 597,40 597,152 0,152" fill="#2a2a2a"/></svg>
      <nav class="abs foot__links"><span>HOME</span><span>ABOUT</span><span>OUR PRODUCTS</span><span>BLOG</span><span>TESTIMONIALS</span><span>CONTACT US</span></nav>
      <div class="abs foot__social"><span></span><span></span><span></span></div>
      <div class="abs foot__copy">Copyrights © 2020 All Rights Reserved</div>
    </div>
  </div>

  <!-- Home page with age verification -->
  <div class="page page--gate">
    <div class="page__content" aria-hidden="true">
      <div class="abs hero"></div>
      <svg class="abs hero__cut" width="597" height="460" viewBox="0 0 597 460"><polygon points="0,320 597,270 597,345 0,345" fill="#000"/></svg>
      <div class="abs nav"></div>
      <div class="abs brand">brightmeadowco.com</div>
      <nav class="abs nav__links"><span class="active">HOME</span><span>ABOUT</span><span>OUR PRODUCTS</span><span>BLOG</span><span>TESTIMONIALS</span><span>CONTACT US &nbsp;|</span></nav>
      <h1 class="abs h hero__title">BRIGHT MEADOW CO</h1>
      <p class="abs hero__sub">Consectetur adipiscing elit, sed do eiusmod<br>tempor incididunt ut labore</p>
      <div class="abs about__img"></div>
      <h2 class="abs h about__title">ABOUT US</h2>
      <p class="abs about__lead">Beatae vitae dicta sunt explicaboemo enim ipsam voluptatem quia</p>
      <div class="abs about__body"><p>Sed ut perspiciatis unde omnis iste natus error sit voluptatem accusantium doloremque laudantium, totam rem aperiam, eaque ipsa quae ab illo inventore veritatis et quasi architecto.</p><p>Dadipisci velit, sed quia non numquam eius modi tempora incidunt ut labore et dolore magnam aliquam.</p></div>
      <div class="abs btn about__btn">READ MORE</div>
      <div class="abs why"></div>
      <h2 class="abs h why__title">WHY CHOOSE US</h2>
      <p class="abs why__body">Eanis iste natus error sit voluptatem accusantium doloremque laudantium, totam rem aperiam, eaque ipsa quae ab illo inventore veritatis et quasi architecto beatae vitae dicta sunt explicabo. Nemo enim ipsam voluptatem quia voluptas sit aspernatur aut odit aut fugit.</p>
      <h2 class="abs h products__title">OUR PRODUCTS</h2>
      <div class="abs card card--active" style="left:45px"><div class="card__img" style="background:linear-gradient(135deg,#f6e2e4,#3a3a3a)"></div><div class="card__price">$7.25 USD</div><div class="btn card__btn">ADD TO CART</div></div>
      <div class="abs card" style="left:218px"><div class="card__img" style="background:linear-gradient(135deg,#bfe6cf,#b0552a)"></div><div class="card__price">$7.25 USD</div><div class="btn card__btn">ADD TO CART</div></div>
      <div class="abs card" style="left:391px"><div class="card__img" style="background:linear-gradient(180deg,#c9a977,#6f7a3a)"></div><div class="card__price">$7.25 USD</div><div class="btn card__btn">ADD TO CART</div></div>
      <div class="abs testi"></div>
      <h2 class="abs h testi__title">TESTIMONIALS</h2>
      <div class="abs quote" style="left:0;width:161px"><div class="quote__avatar" style="left:24px"></div></div>
      <div class="abs quote" style="left:187px;width:224px"><div class="quote__avatar" style="left:88px"></div></div>
      <div class="abs quote" style="left:437px;width:224px"><div class="quote__avatar" style="left:88px"></div></div>
      <h2 class="abs h partners__title">OUR PARTNERS</h2>
      <div class="abs partner" style="left:18px"><i></i>Orbis</div>
      <div class="abs partner partner--on" style="left:122px;width:108px"><i></i>Velda</div>
      <div class="abs partner" style="left:260px"><i></i>Korra</div>
      <div class="abs partner" style="left:378px"><i></i>Lunet</div>
      <svg class="abs foot" width="597" height="152" viewBox="0 0 597 152"><polygon points="0,5 597,40 597,152 0,152" fill="#2a2a2a"/></svg>
      <nav class="abs foot__links"><span>HOME</span><span>ABOUT</span><span>OUR PRODUCTS</span><span>BLOG</span><span>TESTIMONIALS</span><span>CONTACT US</span></nav>
    </div>

    <div class="abs gate" role="dialog" aria-label="Age verification">
      <span class="gate__close">X</span>
      <div class="gate__brand">brightmeadowco.com</div>
      <div class="gate__q">ARE YOU 20 OR OLDER?</div>
      <div class="btn gate__btn" style="left:74px">YES</div>
      <div class="btn gate__btn" style="left:151px">NO</div>
      <p class="gate__note">You must verify that you are 20 Years of age or older to enter this site.</p>
    </div>
  </div>

</div>
</body>
</html>
```